Not for profit organization needs a brochure design

We are an NGO with few on going projects in India namely a special school for Intellectually challenged kids , a charity hospital in underserved area , health and hygeine awareness programs and camps to name a few ..all in India.We need a brochure which will give the reader a quick glimpse of what we do how our beneficiaries have been positively impacted .We need this to able to use for printing as well as digital platform

Target Market(s)

foundations, corporate and individual donors , trusts

Industry/Entity Type

Non Profit

Font styles to use
Sans Serif
Script

Colors
f37122
9ccb3b
0493ce
f59195

Requirements
Must have
• our branding color (orange ,green, blue in that order ), the same font for the name of our NGO , should have the graphic representations of the impact / statistics / numbers we have served or achieved related to our beneficieries ..The details of which are mentioned in the attached document
• The reader should be able to easily understand what our NGO does , what all its involved in and how many have been benefited so far from past 6 years
Nice to have
• to use our own pictures to show our NGO activities and projects and the good work we have been doing ..

```html
<!DOCTYPE html>
<html lang="en">
<head>
<meta charset="utf-8">
<title>Nirmala Jeevan Trust – Brochure</title>
<link href="https://fonts.googleapis.com/css2?family=Open+Sans:wght@400;600;700;800&display=swap" rel="stylesheet">
<style>
:root{
  --orange:#f37122;
  --green:#9ccb3b;
  --blue:#0493ce;
  --pink:#f59195;
  --ink:#3a3a3a;
  --muted:#777;
  --paper:#ffffff;
  --stage:#ececec;
  --photo-warm:#c9a583;
  --photo-cool:#8fa7b8;
  --sans:'Open Sans',Arial,sans-serif;
}
*{box-sizing:border-box;margin:0;padding:0}
html,body{width:1200px;height:2940px;overflow:hidden}
body{background:var(--stage);font-family:var(--sans);color:var(--ink);position:relative}
.spread{position:absolute;left:20px;width:1160px;height:560px;display:flex;background:var(--paper);box-shadow:0 2px 10px rgba(0,0,0,.15)}
.spread--outside{top:890px}
.spread--inside{top:1490px}
.panel{width:290px;height:560px;position:relative;overflow:hidden;padding:12px;border-right:1px solid #eee;font-size:6.5px;line-height:1.45}
.panel:last-child{border-right:none}
.photo{border-radius:2px;background:linear-gradient(135deg,var(--photo-warm),var(--photo-cool))}
.photo--green{background:linear-gradient(135deg,#b6a07c,#6f8f5a)}
.photo--orange{background:linear-gradient(135deg,#e0a060,#9b7a62)}
.tag{display:inline-block;background:var(--orange);color:#fff;font-weight:700;font-size:7px;padding:2px 8px;border-radius:0 8px 8px 0;margin-left:-12px;margin-bottom:4px}
.bar-head{background:var(--green);color:#fff;font-weight:700;font-size:6.8px;padding:2px 6px;margin:6px 0 4px;border-radius:0 8px 8px 0;margin-left:-12px;display:inline-block}
.bar-head--orange{background:var(--orange)}
.bar-head--blue{background:var(--blue)}
.chart{display:block;width:100%}
p{margin-bottom:4px;text-align:justify}
.mini-table{width:100%;border-collapse:collapse;font-size:5.6px}
.mini-table th{background:var(--green);color:#fff;padding:1px 2px;text-align:left}
.mini-table td{padding:1px 2px;border-bottom:1px solid #e5e5e5}
.mini-table tr:nth-child(even) td{background:#f4f9ea}
.wave{position:absolute;left:0;width:100%}
.mission-head{position:absolute;top:0;left:0;width:100%;height:170px}
.mission-body{position:absolute;top:24px;left:14px;right:14px;color:#fff}
.mission-title{font-weight:800;font-size:9px;background:var(--green);display:inline-block;padding:2px 8px;border-radius:8px;margin-bottom:6px}
.mission-list{list-style:none}
.mission-list li{display:flex;gap:5px;align-items:flex-start;margin-bottom:4px}
.dot{flex:none;width:7px;height:7px;border-radius:50%;background:#fff;margin-top:1px}
.icon-grid{display:grid;grid-template-columns:1fr 1fr;gap:8px 10px;margin-top:8px}
.icon-item{display:flex;align-items:center;gap:5px;font-size:6px}
.icon-ring{flex:none;width:16px;height:16px;border-radius:50%;border:2px solid var(--green)}
.icon-item:nth-child(3n+2) .icon-ring{border-color:var(--orange)}
.icon-item:nth-child(3n) .icon-ring{border-color:var(--blue)}
.brand-mark{display:flex;align-items:center;gap:6px;font-weight:700;font-size:8px;color:var(--green)}
.brand-mark .mark{width:16px;height:16px;border-radius:50%;background:var(--green)}
.portrait{width:78px;height:78px;border-radius:50%;border:4px solid var(--orange);margin:6px auto 4px;background:linear-gradient(135deg,#b48b6a,#7c6a5e)}
.story-name{text-align:center;color:var(--orange);font-weight:800;font-size:8px}
.story-sub{text-align:center;color:var(--green);font-weight:700;font-size:7px;margin-bottom:6px}
.two-col{display:grid;grid-template-columns:1fr 1fr;gap:8px}
.founder{display:flex;gap:6px;align-items:flex-start;margin-top:4px}
.founder .photo{flex:none;width:34px;height:34px;border-radius:50%}
.cover{background:#fff}
.cover-circle{position:absolute;top:18px;left:38px;width:220px;height:220px;border-radius:50%;border:7px solid var(--green);outline:5px solid var(--orange);outline-offset:-1px}
.cover-brand{position:absolute;top:268px;left:0;width:100%;display:flex;justify-content:center}
.cover-brand .mark{width:22px;height:22px}
.cover-name{position:absolute;top:300px;left:0;width:100%;text-align:center;font-weight:700;font-size:22px;line-height:1.2;color:var(--green)}
.cover-estd{position:absolute;top:362px;width:100%;left:0;text-align:center;font-size:7px;color:var(--orange);font-weight:700}
.cover-tagline{position:absolute;top:380px;left:30px;right:30px;text-align:center;font-weight:700;font-size:9.5px;color:var(--blue);line-height:1.35}
.cover-web{position:absolute;top:440px;width:100%;left:0;text-align:center;font-size:7px;color:var(--muted)}
.donut-row{display:flex;justify-content:space-between;margin:4px 0}
.legend{display:flex;flex-wrap:wrap;gap:3px 8px;font-size:5.5px;margin-top:2px}
.legend span::before{content:"";display:inline-block;width:5px;height:5px;margin-right:2px;background:var(--c)}
.photo-row{display:flex;gap:4px;margin:4px 0}
.photo-row .photo{flex:1;height:60px}
</style>
</head>
<body>

<section class="spread spread--outside">

  <article class="panel">
    <span class="tag">IMPACT</span>
    <svg class="chart" viewBox="0 0 266 60">
      <line x1="10" y1="54" x2="260" y2="54" stroke="#ccc"/>
      <g fill="var(--orange)">
        <rect x="150" y="40" width="10" height="14"/><rect x="168" y="34" width="10" height="20"/><rect x="186" y="28" width="10" height="26"/><rect x="204" y="20" width="10" height="34"/><rect x="222" y="14" width="10" height="40"/><rect x="240" y="6" width="10" height="48"/>
      </g>
      <polyline points="155,38 173,31 191,25 209,17 227,11 245,4" fill="none" stroke="var(--green)" stroke-width="1.5"/>
      <text x="10" y="20" font-size="6" fill="var(--ink)">Beneficiaries served</text>
      <text x="10" y="29" font-size="6" fill="var(--ink)">over six years</text>
    </svg>
    <span class="bar-head">PATIENTS TREATED BY YEAR</span>
    <table class="mini-table">
      <tr><th>Year</th><th>OPD</th><th>IPD</th><th>Camps</th><th>Total</th></tr>
      <tr><td>2012</td><td>4210</td><td>310</td><td>12</td><td>4532</td></tr>
      <tr><td>2013</td><td>5120</td><td>355</td><td>15</td><td>5490</td></tr>
      <tr><td>2014</td><td>6030</td><td>402</td><td>18</td><td>6450</td></tr>
    </table>
    <span class="bar-head">STUDENTS ENROLLED AT SCHOOL</span>
    <svg class="chart" viewBox="0 0 266 70">
      <line x1="6" y1="62" x2="262" y2="62" stroke="#ccc"/>
      <rect x="20" y="40" width="8" height="22" fill="var(--orange)"/><rect x="29" y="30" width="8" height="32" fill="var(--green)"/><rect x="38" y="46" width="8" height="16" fill="var(--blue)"/>
      <rect x="80" y="34" width="8" height="28" fill="var(--orange)"/><rect x="89" y="24" width="8" height="38" fill="var(--green)"/><rect x="98" y="42" width="8" height="20" fill="var(--blue)"/>
      <rect x="140" y="28" width="8" height="34" fill="var(--orange)"/><rect x="149" y="16" width="8" height="46" fill="var(--green)"/><rect x="158" y="38" width="8" height="24" fill="var(--blue)"/>
      <rect x="200" y="20" width="8" height="42" fill="var(--orange)"/><rect x="209" y="8" width="8" height="54" fill="var(--green)"/><rect x="218" y="32" width="8" height="30" fill="var(--blue)"/>
    </svg>
    <span class="bar-head">HEALTH CAMPS CONDUCTED</span>
    <svg class="chart" viewBox="0 0 266 70">
      <line x1="6" y1="62" x2="262" y2="62" stroke="#ccc"/>
      <g fill="var(--pink)"><rect x="30" y="30" width="14" height="32"/><rect x="90" y="22" width="14" height="40"/><rect x="150" y="14" width="14" height="48"/><rect x="210" y="8" width="14" height="54"/></g>
      <g fill="#e24a4a"><rect x="46" y="40" width="6" height="22"/><rect x="106" y="34" width="6" height="28"/><rect x="166" y="28" width="6" height="34"/><rect x="226" y="22" width="6" height="40"/></g>
    </svg>
    <div class="photo photo--orange" role="img" aria-label="Photo of a smiling schoolchild" style="position:absolute;left:70px;bottom:18px;width:70px;height:60px;border-radius:50%"></div>
    <svg class="wave" style="bottom:0;height:40px" viewBox="0 0 290 40" preserveAspectRatio="none">
      <path d="M0 18 Q80 40 170 20 T290 14 V40 H0Z" fill="var(--orange)"/>
      <path d="M0 28 Q90 44 180 28 T290 24 V40 H0Z" fill="var(--blue)"/>
    </svg>
  </article>

  <article class="panel">
    <svg class="mission-head" viewBox="0 0 290 170" preserveAspectRatio="none">
      <path d="M0 0 H290 V130 Q150 180 0 140Z" fill="var(--blue)"/>
      <path d="M0 140 Q150 180 290 130 V138 Q150 188 0 148Z" fill="var(--green)"/>
    </svg>
    <div class="mission-body">
      <div class="mission-title">OUR MISSION</div>
      <ul class="mission-list">
        <li><span class="dot"></span>To offer free and low cost medical care to families in remote villages.</li>
        <li><span class="dot"></span>To run a special school giving care and skills to children with intellectual disability.</li>
        <li><span class="dot"></span>To hold health and hygiene awareness camps in schools and villages.</li>
        <li><span class="dot"></span>To train local youth as health volunteers for their own community.</li>
      </ul>
    </div>
    <div class="photo-row" style="margin-top:160px">
      <div class="photo" role="img" aria-label="Photo of a doctor examining a patient"></div>
      <div class="photo photo--green" role="img" aria-label="Photo of the hospital front"></div>
    </div>
    <span class="bar-head bar-head--blue">SERVICES WE PROVIDE</span>
    <div class="icon-grid">
      <div class="icon-item"><span class="icon-ring"></span>General outpatient care</div>
      <div class="icon-item"><span class="icon-ring"></span>Maternal and child health</div>
      <div class="icon-item"><span class="icon-ring"></span>Free medicines</div>
      <div class="icon-item"><span class="icon-ring"></span>Special education</div>
      <div class="icon-item"><span class="icon-ring"></span>Physiotherapy</div>
      <div class="icon-item"><span class="icon-ring"></span>Vocational training</div>
      <div class="icon-item"><span class="icon-ring"></span>Eye screening camps</div>
      <div class="icon-item"><span class="icon-ring"></span>Hygiene awareness</div>
    </div>
    <p style="margin-top:12px">Every rupee you give reaches a child, a mother or an elder who has nowhere else to turn for care and learning.</p>
    <div class="brand-mark" style="margin-top:10px"><span class="mark"></span>Nirmala Jeevan Trust</div>
  </article>

  <article class="panel">
    <div class="portrait" role="img" aria-label="Portrait of the elderly woman the trust is named after"></div>
    <div class="story-name">SAVITRI AMMAL (NIRMALA)</div>
    <div class="story-sub">THE STORY BEHIND THE NAME “NIRMALA”</div>
    <p>The trust carries the name of a mother who fed every hungry visitor at her door and nursed the sick of her village without asking for anything back. Her children started this work in her memory so that her kindness may keep reaching the people who need it most.</p>
    <div class="two-col">
      <div><span class="bar-head">MISSION</span><p>Quality care and learning for the poor and the differently abled, delivered with dignity.</p></div>
      <div><span class="bar-head bar-head--orange">VISION</span><p>A healthy, inclusive village where no one is left without care or a chance to learn.</p></div>
    </div>
    <span class="bar-head">MESSAGE FROM THE FOUNDER</span>
    <div class="founder">
      <div class="photo" role="img" aria-label="Photo of the founder"></div>
      <p>Over six years our small team has grown into a hospital, a school and a network of camps. We thank every donor who walked with us and invite you to join.</p>
    </div>
    <span class="bar-head bar-head--orange">OUR COMMITMENT</span>
    <p>We keep costs low, report openly to our donors and measure every programme by the lives it changes.</p>
    <p>We welcome visits from partners to see our work in person.</p>
  </article>

  <article class="panel cover">
    <svg class="wave" style="top:0;height:60px" viewBox="0 0 290 60" preserveAspectRatio="none">
      <path d="M0 0 H290 V20 Q150 60 0 30Z" fill="var(--green)" opacity=".25"/>
    </svg>
    <div class="cover-circle photo" role="img" aria-label="Photo of volunteers giving care to village patients"></div>
    <div class="cover-brand"><div class="brand-mark"><span class="mark"></span></div></div>
    <div class="cover-name">Nirmala Jeevan Trust</div>
    <div class="cover-estd">ESTD. 2006</div>
    <div class="cover-tagline">BRINGING MEDICINE AND LEARNING TO THE FAMILIES WHO NEED IT MOST, WITH KINDNESS AND DEDICATION</div>
    <div class="cover-web">www.nirmalajeevan.org</div>
    <svg class="wave" style="bottom:0;height:70px" viewBox="0 0 290 70" preserveAspectRatio="none">
      <path d="M0 30 Q140 0 290 34 V70 H0Z" fill="var(--orange)"/>
      <path d="M0 44 Q140 16 290 48 V70 H0Z" fill="var(--green)"/>
      <path d="M0 58 Q140 34 290 60 V70 H0Z" fill="var(--blue)"/>
    </svg>
  </article>
</section>

<section class="spread spread--inside">

  <article class="panel">
    <span class="bar-head">RECREATIONAL ACTIVITIES</span>
    <div class="donut-row">
      <svg width="54" height="54" viewBox="0 0 42 42"><circle cx="21" cy="21" r="15" fill="none" stroke="#e6e6e6" stroke-width="7"/><circle cx="21" cy="21" r="15" fill="none" stroke="var(--blue)" stroke-width="7" stroke-dasharray="70 95" transform="rotate(-90 21 21)"/></svg>
      <svg width="54" height="54" viewBox="0 0 42 42"><circle cx="21" cy="21" r="15" fill="none" stroke="#e6e6e6" stroke-width="7"/><circle cx="21" cy="21" r="15" fill="none" stroke="var(--green)" stroke-width="7" stroke-dasharray="55 95" transform="rotate(-90 21 21)"/></svg>
      <svg width="54" height="54" viewBox="0 0 42 42"><circle cx="21" cy="21" r="15" fill="none" stroke="#e6e6e6" stroke-width="7"/><circle cx="21" cy="21" r="15" fill="none" stroke="var(--blue)" stroke-width="7" stroke-dasharray="80 95" transform="rotate(-90 21 21)"/></svg>
      <svg width="54" height="54" viewBox="0 0 42 42"><circle cx="21" cy="21" r="15" fill="none" stroke="#e6e6e6" stroke-width="7"/><circle cx="21" cy="21" r="15" fill="none" stroke="var(--orange)" stroke-width="7" stroke-dasharray="62 95" transform="rotate(-90 21 21)"/></svg>
    </div>
    <div class="legend"><span style="--c:var(--blue)">Yoga</span><span style="--c:var(--green)">Sports</span><span style="--c:var(--blue)">Music</span><span style="--c:var(--orange)">Art</span></div>
    <span class="bar-head">SCHOOL AND OTHER SERVICES PROVIDED</span>
    <svg class="chart" viewBox="0 0 266 100">
      <line x1="6" y1="92" x2="262" y2="92" stroke="#ccc"/>
      <rect x="18" y="40" width="9" height="52" fill="var(--orange)"/><rect x="28" y="20" width="9" height="72" fill="#f3c623"/><rect x="38" y="54" width="9" height="38" fill="var(--blue)"/>
      <rect x="80" y="34" width="9" height="58" fill="var(--orange)"/><rect x="90" y="14" width="9" height="78" fill="#f3c623"/><rect x="100" y="50" width="9" height="42" fill="var(--blue)"/>
      <rect x="142" y="30" width="9" height="62" fill="var(--orange)"/><rect x="152" y="10" width="9" height="82" fill="#f3c623"/><rect x="162" y="44" width="9" height="48" fill="var(--blue)"/>
      <rect x="204" y="26" width="9" height="66" fill="var(--orange)"/><rect x="214" y="6" width="9" height="86" fill="#f3c623"/><rect x="224" y="40" width="9" height="52" fill="var(--blue)"/>
    </svg>
    <div class="photo photo--orange" role="img" aria-label="Group photo of schoolchildren in uniform" style="height:60px;margin:6px 0"></div>
    <span class="bar-head">ACHIEVEMENT OF CHILDREN</span>
    <svg class="chart" viewBox="0 0 266 130">
      <line x1="6" y1="120" x2="262" y2="120" stroke="#ccc"/>
      <rect x="24" y="90" width="22" height="30" fill="var(--blue)"/><rect x="24" y="70" width="22" height="20" fill="#e2217a"/><rect x="24" y="55" width="22" height="15" fill="var(--green)"/><rect x="24" y="44" width="22" height="11" fill="#7b4cb0"/>
      <rect x="84" y="84" width="22" height="36" fill="var(--blue)"/><rect x="84" y="60" width="22" height="24" fill="#e2217a"/><rect x="84" y="42" width="22" height="18" fill="var(--green)"/><rect x="84" y="30" width="22" height="12" fill="#7b4cb0"/>
      <rect x="144" y="80" width="22" height="40" fill="var(--blue)"/><rect x="144" y="52" width="22" height="28" fill="#e2217a"/><rect x="144" y="32" width="22" height="20" fill="var(--green)"/><rect x="144" y="18" width="22" height="14" fill="#7b4cb0"/>
      <rect x="204" y="76" width="22" height="44" fill="var(--blue)"/><rect x="204" y="44" width="22" height="32" fill="#e2217a"/><rect x="204" y="22" width="22" height="22" fill="var(--green)"/><rect x="204" y="6" width="22" height="16" fill="#7b4cb0"/>
      <g font-size="6" fill="var(--ink)"><text x="24" y="128">2011</text><text x="84" y="128">2012</text><text x="144" y="128">2013</text><text x="204" y="128">2014</text></g>
    </svg>
    <div class="legend"><span style="--c:var(--blue)">Self care</span><span style="--c:#e2217a">Reading</span><span style="--c:var(--green)">Social skills</span><span style="--c:#7b4cb0">Work skills</span></div>
  </article>

  <article class="panel">
    <span class="bar-head">SPECIAL SCHOOL OUTCOMES</span>
    <svg class="chart" viewBox="0 0 266 130">
      <g transform="translate(60 35)"><circle r="24" fill="none" stroke="var(--orange)" stroke-width="11" stroke-dasharray="60 151"/><circle r="24" fill="none" stroke="var(--green)" stroke-width="11" stroke-dasharray="50 151" stroke-dashoffset="-60"/><circle r="24" fill="none" stroke="var(--blue)" stroke-width="11" stroke-dasharray="41 151" stroke-dashoffset="-110"/></g>
      <g transform="translate(200 35)"><circle r="24" fill="none" stroke="var(--pink)" stroke-width="11" stroke-dasharray="70 151"/><circle r="24" fill="none" stroke="#7b4cb0" stroke-width="11" stroke-dasharray="45 151" stroke-dashoffset="-70"/><circle r="24" fill="none" stroke="var(--blue)" stroke-width="11" stroke-dasharray="36 151" stroke-dashoffset="-115"/></g>
      <g transform="translate(60 100)"><circle r="24" fill="none" stroke="var(--green)" stroke-width="11" stroke-dasharray="80 151"/><circle r="24" fill="none" stroke="var(--orange)" stroke-width="11" stroke-dasharray="71 151" stroke-dashoffset="-80"/></g>
      <g transform="translate(200 100)"><circle r="24" fill="none" stroke="#e2217a" stroke-width="11" stroke-dasharray="64 151"/><circle r="24" fill="none" stroke="var(--blue)" stroke-width="11" stroke-dasharray="87 151" stroke-dashoffset="-64"/></g>
    </svg>
    <p>Children at our school learn daily living skills, speech and simple crafts. Parents receive counselling so that progress continues at home.</p>
    <span class="bar-head bar-head--orange">SCHOOL AT A GLANCE</span>
    <p>Sixty four children attend each day, supported by eleven trained teachers, two therapists and a visiting doctor.</p>
    <div class="photo-row">
      <div class="photo photo--green" role="img" aria-label="Photo of children at a classroom activity"></div>
      <div class="photo" role="img" aria-label="Photo of a teacher with a student"></div>
    </div>
    <span class="bar-head">PARENT SUPPORT</span>
    <p>Monthly parent meetings share progress, home exercises and news of government benefits that families may claim.</p>
    <p>Many parents now volunteer at the school and help new families settle in.</p>
    <svg class="wave" style="bottom:0;height:34px" viewBox="0 0 290 34" preserveAspectRatio="none">
      <path d="M0 14 Q140 34 290 10 V34 H0Z" fill="var(--green)"/>
    </svg>
  </article>

  <article class="panel">
    <span class="bar-head bar-head--orange">OUR CHARITY HOSPITAL</span>
    <p>Opened in a village with no doctor for miles, our hospital now serves thousands each year with outpatient care, minor surgery, lab tests and free medicine for the poorest families.</p>
    <span class="bar-head">HOSPITAL STATISTICS</span>
    <table class="mini-table">
      <tr><th>Service</th><th>2011</th><th>2012</th><th>2013</th><th>2014</th></tr>
      <tr><td>Outpatients</td><td>3820</td><td>4210</td><td>5120</td><td>6030</td></tr>
      <tr><td>Inpatients</td><td>260</td><td>310</td><td>355</td><td>402</td></tr>
      <tr><td>Lab tests</td><td>1410</td><td>1690</td><td>2040</td><td>2380</td></tr>
      <tr><td>Deliveries</td><td>48</td><td>62</td><td>71</td><td>85</td></tr>
      <tr><td>Surgeries</td><td>32</td><td>40</td><td>46</td><td>58</td></tr>
      <tr><td>Eye checks</td><td>520</td><td>610</td><td>730</td><td>880</td></tr>
      <tr><td>Dental</td><td>210</td><td>260</td><td>300</td><td>350</td></tr>
    </table>
    <div class="photo-row">
      <div class="photo" role="img" aria-label="Photo of patients waiting at the hospital"></div>
      <div class="photo photo--orange" role="img" aria-label="Photo of staff at the reception desk"></div>
    </div>
    <span class="bar-head">HEALTH AWARENESS PROGRAMS</span>
    <p>Our team visits schools and villages to teach hand washing, safe water, nutrition and menstrual hygiene.</p>
    <div class="photo" role="img" aria-label="Photo of a doctor checking a woman at a camp" style="height:80px;margin-top:4px"></div>
  </article>

  <article class="panel">
    <div class="photo-row">
      <div class="photo photo--green" role="img" aria-label="Photo of a village health camp"></div>
      <div class="photo" role="img" aria-label="Photo of volunteers with villagers"></div>
    </div>
    <span class="bar-head">HEALTH CAMPS</span>
    <p>Free camps bring doctors, medicines and screening to hamlets far from any clinic. Serious cases are referred to our hospital at no cost.</p>
    <span class="bar-head bar-head--orange">HYGIENE KITS DISTRIBUTED</span>
    <p>Kits with soap, towels and sanitary pads reach girls in rural schools every term.</p>
    <svg class="chart" viewBox="0 0 266 90">
      <line x1="6" y1="82" x2="262" y2="82" stroke="#ccc"/>
      <rect x="24" y="50" width="14" height="32" fill="var(--green)"/><rect x="40" y="60" width="14" height="22" fill="var(--blue)"/>
      <rect x="84" y="40" width="14" height="42" fill="var(--green)"/><rect x="100" y="52" width="14" height="30" fill="var(--blue)"/>
      <rect x="144" y="28" width="14" height="54" fill="var(--green)"/><rect x="160" y="42" width="14" height="40" fill="var(--blue)"/>
      <rect x="204" y="12" width="14" height="70" fill="var(--green)"/><rect x="220" y="30" width="14" height="52" fill="var(--blue)"/>
    </svg>
    <div class="legend"><span style="--c:var(--green)">Kits given</span><span style="--c:var(--blue)">Schools reached</span></div>
    <span class="bar-head">HOW YOU CAN HELP</span>
    <p>Sponsor a child, fund a camp or donate medicines. Write to us through www.nirmalajeevan.org to learn more.</p>
    <div class="photo photo--orange" role="img" aria-label="Photo of children and volunteers at a camp" style="height:70px;margin-top:4px"></div>
  </article>
</section>

</body>
</html>
```